Business Card Design

We are a General Practice - Family medicine
We also have Allied Health professionals working within our team

Industry/Entity Type

Business

Contact Information for Business Card

Front of the card to display:

BRAMBLEWICK MEDICAL
PHONE 6348 2917

5/41 Fennimore Parade
Launceston Tasmania 7284

Back of the card to display:

My Appointments
Date:
Time:
With:

Please remember to phone us on 6348 2917 to cancel your appointment if you can't keep it.
A fee applied to missed appointments

```html
<!DOCTYPE html>
<html lang="en">
<head>
<meta charset="utf-8">
<title>Bramblewick Medical – Business Card</title>
<link href="https://fonts.googleapis.com/css2?family=Barlow:wght@400;500&family=Questrial&display=swap" rel="stylesheet">
<style>
  :root {
    --stage: #000000;
    --card: #ffffff;
    --band-blue: #52b0e0;
    --band-green: #9acd55;
    --brand-blue: #41aee3;
    --phone-blue: #138fd4;
    --ink: #111111;
    --grey: #595959;
    --rule: #222222;
  }
  * { margin: 0; padding: 0; box-sizing: border-box; }
  html, body {
    width: 1200px; height: 1000px; overflow: hidden;
    background: var(--stage);
  }
  .stage { position: relative; width: 1200px; height: 1000px; }
  .card {
    position: absolute; left: 251px; width: 698px;
    background: var(--card); overflow: hidden;
  }
  .card--front { top: 62px; height: 427px; }
  .card--back { top: 496px; height: 431px; }

  .accent-band {
    position: absolute; left: 0; width: 100%; height: 44px;
    background: linear-gradient(90deg, var(--band-green), var(--band-blue));
    opacity: 0.85;
  }
  .accent-band--top { top: 0; }
  .accent-band--bottom {
    bottom: 0;
    background: linear-gradient(90deg, var(--band-blue), var(--band-green));
  }

  .centered { position: absolute; left: 0; width: 100%; text-align: center; }

  .brand-name {
    top: 146px;
    font-family: "Barlow", sans-serif; font-weight: 400;
    font-size: 38px; color: var(--brand-blue); letter-spacing: -0.3px;
  }
  .front-phone {
    top: 250px;
    font-family: "Barlow", sans-serif; font-weight: 500;
    font-size: 38px; color: var(--phone-blue);
    display: flex; justify-content: center; align-items: center; gap: 10px;
  }
  .front-phone svg { width: 22px; height: 30px; fill: var(--phone-blue); }
  .address {
    top: 318px;
    font-family: "Questrial", sans-serif; font-style: normal;
    font-size: 21px; line-height: 25px; color: var(--grey);
  }

  .appointments-title {
    top: 96px;
    font-family: "Barlow", sans-serif; font-weight: 500;
    font-size: 22px; color: var(--brand-blue);
  }
  .appointment-field {
    position: absolute; left: 162px; width: 376px; height: 24px;
    display: flex; align-items: center;
    font-family: "Barlow", sans-serif; font-weight: 500;
    font-size: 19px; color: var(--ink);
  }
  .appointment-field::before {
    content: ""; width: 5px; height: 5px; border-radius: 50%;
    background: var(--rule); margin-right: 1px;
  }
  .appointment-field .lead {
    width: 12px; height: 1px; background: var(--rule); margin-right: 4px;
  }
  .appointment-field .label { margin-right: 6px; }
  .appointment-field .blank {
    flex: 1; height: 1px; background: var(--rule); position: relative;
  }
  .appointment-field .blank::after {
    content: ""; position: absolute; right: -2px; top: -2px;
    width: 5px; height: 5px; border-radius: 50%; background: var(--rule);
  }
  .field--date { top: 146px; }
  .field--time { top: 201px; }
  .field--with { top: 257px; }

  .cancel-note {
    top: 309px;
    font-family: "Barlow", sans-serif; font-weight: 500;
    font-size: 13.5px; line-height: 22px; color: var(--ink);
  }
  .cancel-note .note-phone { font-size: 16px; color: var(--phone-blue); }
</style>
</head>
<body>
<main class="stage">

  <section class="card card--front" aria-label="Card front">
    <div class="accent-band accent-band--top" role="img" aria-label="Blue and green decorative wave band"></div>

    <h1 class="centered brand-name">Bramblewick Medical</h1>

    <p class="centered front-phone">
      <svg viewBox="0 0 22 30" aria-label="Phone"><path d="M6 1 L10 1 L11 8 L8 10 Q8 16 12 20 L15 18 L20 22 L19 27 Q16 30 11 27 Q3 20 2 10 Q2 4 6 1 Z"/></svg>
      <span>6348 2917</span>
    </p>

    <address class="centered address">
      5/41 Fennimore Parade Launceston<br>Tasmania 7284
    </address>

    <div class="accent-band accent-band--bottom" role="img" aria-label="Blue and green decorative wave band"></div>
  </section>

  <section class="card card--back" aria-label="Card back">
    <div class="accent-band accent-band--top" role="img" aria-label="Blue and green decorative wave band"></div>

    <h2 class="centered appointments-title">My Appointments</h2>

    <div class="appointment-field field--date"><span class="lead"></span><span class="label">Date :</span><span class="blank"></span></div>
    <div class="appointment-field field--time"><span class="lead"></span><span class="label">Time :</span><span class="blank"></span></div>
    <div class="appointment-field field--with"><span class="lead"></span><span class="label">With :</span><span class="blank"></span></div>

    <p class="centered cancel-note">
      Please remember to phone us on <span class="note-phone">6348 2917</span> to cancel your appointment if you can't keep it.<br>
      A fee applied to missed appointments
    </p>

    <div class="accent-band accent-band--bottom" role="img" aria-label="Blue and green decorative wave band"></div>
  </section>

</main>
</body>
</html>
```